Brantley Fuel Retro Website Design

Have a logo. Need a website design to go along with the logo design. Full Design Specs are here: https://files.quorvand.net/doc/8QmXr2Lp-47tn806Hw3ZkYvB-Rs5cJ9aE/view

Target Market(s)

Independent Gas Station Owners

Number of Pages Required

1 page

Font styles to use
Sans Serif

Colors

Designer to choose colors to be used in the design.

```html
<!DOCTYPE html>
<html lang="en">
<head>
<meta charset="utf-8">
<title>Brantley Fuel</title>
<link href="https://fonts.googleapis.com/css2?family=Arvo:wght@400;700&family=Lato:wght@400;700&display=swap" rel="stylesheet">
<style>
:root{
  --red:#e0252b;
  --ink:#2b2b2b;
  --text:#3c3c3c;
  --muted:#6b6b6b;
  --paper:#eeeeee;
  --card:#ffffff;
  --bar:#5a5a5a;
  --bar-dark:#3f3f3f;
  --footer:#4a4a4a;
  --footer-text:#e6e6e6;
  --star:#f2a623;
}
*{box-sizing:border-box;margin:0;padding:0}
html,body{width:1200px;height:4115px;overflow:hidden}
body{position:relative;background:var(--paper);font-family:"Lato",Arial,sans-serif;color:var(--text);font-size:13.5px;line-height:1.55}
.abs{position:absolute}
.slab{font-family:"Arvo",Georgia,serif;color:var(--ink);font-weight:400}

/* header */
.hero-photo{left:0;top:0;width:1200px;height:630px;background:linear-gradient(180deg,#b9bcbf 0%,#c9cbcd 38%,#a7a6a3 52%,#bdbcba 70%,var(--paper) 100%)}
.phone{left:80px;top:22px;display:flex;align-items:center;gap:10px;font-size:15px;color:var(--ink)}
.phone .dot{width:24px;height:24px;border-radius:50%;background:#3a3a3a;display:flex;align-items:center;justify-content:center}
.social{display:flex;gap:8px}
.social span{width:24px;height:24px;border-radius:50%;background:var(--red);display:block}
.social.top{right:68px;top:22px}
.navbar{left:58px;top:70px;width:1084px;height:56px}
.nav{left:80px;top:70px;width:1060px;height:46px;display:flex;align-items:center;font-size:14px;color:#f2f2f2;letter-spacing:.5px}
.nav a{position:absolute;top:0;height:46px;line-height:46px;text-align:center;color:inherit;text-decoration:none}
.nav a.active{background:var(--red);color:#fff}
.nav .sep{position:absolute;top:12px;width:1px;height:22px;background:#7a7a7a}
.brand-badge{left:530px;top:18px;width:146px;height:146px;border-radius:50%;background:#fff;border:4px solid #3a3a3a;display:flex;align-items:center;justify-content:center;text-align:center}
.brand-badge span{font-family:"Arvo",Georgia,serif;font-weight:700;font-size:20px;line-height:1.1;color:var(--red)}

/* sections */
.section-title{left:0;width:1200px;text-align:center;font-size:35px;letter-spacing:3px}
.about-sub{left:82px;top:770px;font-size:33px;border-bottom:2px solid #444;padding-bottom:0;line-height:1.2}
.about-text{left:82px;top:826px;width:490px;font-size:13.5px}
.about-text p+p{margin-top:20px}
.btn{background:var(--red);color:#fff;text-align:center;font-size:14px;letter-spacing:.5px}
.about-photo-shadow{left:617px;top:752px;width:499px;height:339px;background:#d8d8d8}
.about-photo{left:601px;top:736px;width:499px;height:339px;background:linear-gradient(160deg,#bfbbb2,#8f8c85 60%,#6c6a65)}

.frame{background:#fff;padding:12px}
.frame .ph{width:100%;height:100%}
.svc{width:500px;text-align:center}
.svc h3{font-family:"Arvo",Georgia,serif;font-weight:400;font-size:22px;color:var(--ink);letter-spacing:1px;margin:6px 0 16px}
.svc p{font-size:13.5px;line-height:1.6}
.svc svg{display:block;margin:0 auto}

/* blogs */
.blog{top:2853px;width:323px;height:387px;background:var(--card)}
.blog .ph{width:323px;height:197px}
.blog .link{position:absolute;left:134px;top:174px;width:54px;height:54px;border-radius:50%;background:#333;border:4px solid #fff;display:flex;align-items:center;justify-content:center}
.blog .head{position:absolute;left:26px;top:244px;width:271px;display:flex;justify-content:space-between;align-items:baseline}
.blog .head h4{font-family:"Arvo",Georgia,serif;font-weight:400;font-size:19px;color:var(--ink)}
.blog .head time{font-family:"Arvo",Georgia,serif;font-size:12px;color:var(--muted);letter-spacing:.5px}
.blog p{position:absolute;left:26px;top:283px;width:275px;font-size:13px;line-height:1.35}
.blog .meta{position:absolute;left:28px;top:345px;width:270px;display:flex;font-size:13px;align-items:center}
.blog .meta .read{flex:1}
.blog .meta .count{display:flex;align-items:center;gap:5px;margin-left:16px}

/* testimonials */
.quote-card{top:3437px;height:222px;background:var(--card)}
.quote-mark{top:3416px;width:45px;height:43px;background:var(--red);color:#fff;font-family:"Arvo",Georgia,serif;font-size:34px;font-weight:700;text-align:center;line-height:52px}
.avatar{width:112px;height:112px;border-radius:50%;background:radial-gradient(circle at 50% 40%,#c9a887,#7a5a40 70%,#4b3a2c)}
.quote-name{font-family:"Arvo",Georgia,serif;font-size:20px;color:var(--ink)}
.quote-text{width:300px;font-size:12.5px;line-height:1.3}
.stars{display:flex;gap:6px}
.dots{left:582px;top:3691px;display:flex;gap:5px}
.dots span{width:8px;height:8px;border-radius:50%;background:#999}
.dots span:first-child{background:var(--red)}

/* footer */
.footer{left:0;top:3745px;width:1200px;height:300px;background:var(--footer);color:var(--footer-text)}
.foot-badge{left:101px;top:3824px;width:160px;height:160px;border-radius:50%;background:#fff;border:5px solid #3a3a3a;display:flex;align-items:center;justify-content:center;text-align:center}
.foot-badge span{font-family:"Arvo",Georgia,serif;font-weight:700;font-size:22px;line-height:1.1;color:var(--red)}
.foot-h{font-family:"Arvo",Georgia,serif;font-size:19px;color:#fff}
.foot-list{list-style:none;font-size:13px;color:var(--footer-text)}
.foot-list li{height:22px;line-height:22px}
.foot-list.links li::before{content:">";margin-right:14px}
.contact li{display:flex;gap:10px;align-items:flex-start;line-height:22px;height:auto}
.contact svg{flex:none;margin-top:5px}
.news-input{left:862px;top:3901px;width:256px;height:33px;border-radius:17px;background:#fff;color:#888;font-size:13px;line-height:33px;padding-left:18px}
.subscribe{left:862px;top:3949px;width:131px;height:33px;border-radius:17px;background:var(--red);color:#fff;font-size:13px;text-align:center;line-height:33px}
.copyright{left:80px;top:4079px;font-size:13px;color:var(--ink)}
.social.bottom{right:84px;top:4077px}
</style>
</head>
<body>

<!-- header -->
<div class="abs hero-photo" role="img" aria-label="Photograph of the fuel company's white metal storefront with pickup trucks and cars parked out front"></div>

<div class="abs phone">
  <span class="dot"><svg width="12" height="12" viewBox="0 0 24 24"><path fill="#fff" d="M6.6 10.8a15.1 15.1 0 0 0 6.6 6.6l2.2-2.2a1 1 0 0 1 1-.25 11.4 11.4 0 0 0 3.6.57 1 1 0 0 1 1 1V20a1 1 0 0 1-1 1A17 17 0 0 1 3 4a1 1 0 0 1 1-1h3.5a1 1 0 0 1 1 1c0 1.25.2 2.45.57 3.57a1 1 0 0 1-.25 1z"/></svg></span>
  014-2287-55
</div>
<div class="abs social top"><span></span><span></span><span></span><span></span></div>

<svg class="abs navbar" viewBox="0 0 1084 56" width="1084" height="56">
  <polygon points="0,12 22,12 22,56 10,48 14,30" fill="var(--bar-dark)"/>
  <polygon points="1084,12 1062,12 1062,56 1074,48 1070,30" fill="var(--bar-dark)"/>
  <rect x="22" y="0" width="1040" height="46" fill="var(--bar)"/>
</svg>
<nav class="abs nav">
  <a class="active" style="left:0;width:146px">Home</a>
  <a style="left:174px;width:100px">About</a>
  <span class="sep" style="left:290px"></span>
  <a style="left:320px;width:106px">Services</a>
  <span class="sep" style="left:445px"></span>
  <span class="sep" style="left:615px"></span>
  <a style="left:635px;width:142px">Testimonials</a>
  <span class="sep" style="left:782px"></span>
  <a style="left:810px;width:66px">Blog</a>
  <span class="sep" style="left:895px"></span>
  <a style="left:918px;width:94px">Contact</a>
</nav>
<div class="abs brand-badge"><span>Brantley<br>Fuel</span></div>

<!-- about -->
<h2 class="abs slab section-title" style="top:660px">About us</h2>
<h3 class="abs slab about-sub">What wo do</h3>
<div class="abs about-text">
  <p>Lorem Ipsum is simply dummy text of the printing and typesetting industry Ipsum has been the industry's standard dummy text ever since the 1500s,</p>
  <p>when an unknown printer took a galley of type and scrambled it to make a type a specimen book. It has survived not only five centuries, but also the leap into plane electronic typesetting, remaining essentially unchanged.&nbsp; It was popularised in the 1960s</p>
</div>
<div class="abs btn" style="left:80px;top:998px;width:176px;height:48px;line-height:48px">Read More</div>
<div class="abs about-photo-shadow"></div>
<div class="abs about-photo" role="img" aria-label="Vintage sepia photograph of the original service station with fuel tanks"></div>

<!-- services -->
<h2 class="abs slab section-title" style="top:1144px">Services</h2>

<div class="abs frame" style="left:82px;top:1232px;width:502px;height:379px">
  <div class="ph" role="img" aria-label="Photograph of a white fuel delivery tank truck" style="background:linear-gradient(180deg,#cdd3d6 0%,#c4c6c4 45%,#8e8f8c 70%,#6f706c 100%)"></div>
</div>
<div class="abs svc" style="left:614px;top:1300px">
  <svg width="116" height="70" viewBox="0 0 116 70" fill="none" stroke="#222" stroke-width="3.5">
    <rect x="14" y="12" width="56" height="30" rx="15"/><path d="M34 12V4h16v8"/>
    <path d="M8 42h98V32l-10-14H76v24"/><path d="M84 22h8l6 10H84z"/>
    <circle cx="24" cy="54" r="7"/><circle cx="46" cy="54" r="7"/><circle cx="90" cy="54" r="7"/>
  </svg>
  <h3>Fuel Delivery</h3>
  <p>Brantley Fuel provides fuel delivery for independent gas stations, convenience stores, construction sites or any other commercial need.&nbsp; If you are looking for gasoline, high sulfer diesel fuel, farm diesel or other bulk fuel delivered to your business, we will take care of you!</p>
</div>

<div class="abs frame" style="left:621px;top:1611px;width:501px;height:381px">
  <div class="ph" role="img" aria-label="Photograph of store shelves stocked with motor oil and washer fluid bottles" style="background:linear-gradient(135deg,#cfd3d8 0%,#6d7d6a 40%,#2f3032 70%,#8a5a3a 100%)"></div>
</div>
<div class="abs svc" style="left:84px;top:1684px">
  <svg width="62" height="76" viewBox="0 0 62 76" fill="none" stroke="#222" stroke-width="3.5">
    <rect x="24" y="14" width="32" height="58"/><path d="M32 14V4h16v10"/>
    <path d="M16 40c-8 12-12 18-12 23a12 12 0 0 0 24 0c0-5-4-11-12-23z" fill="#eee"/>
  </svg>
  <h3>Oil</h3>
  <p>Looking for speciality auto, tractor, tractor trailer, aviation or other commercial oils and lubricants Brantley Fuel can help!&nbsp; Just call one of our customer oriented staff and we will get what you need quick!&nbsp; We have a complete line of aviation oils and lubricants as well as gear lubricants, greases, oils and more!</p>
</div>

<div class="abs frame" style="left:85px;top:1979px;width:502px;height:379px">
  <div class="ph" role="img" aria-label="Photograph of a large silver fuel storage tank on a trailer" style="background:linear-gradient(180deg,#b8bcbd 0%,#d9dbdc 35%,#a4a6a7 65%,#5d5f5e 100%)"></div>
</div>
<div class="abs svc" style="left:614px;top:2052px">
  <svg width="118" height="92" viewBox="0 0 118 92" fill="none" stroke="#222" stroke-width="3.5">
    <rect x="6" y="16" width="106" height="50" rx="25"/><path d="M70 16v50M84 16v50"/><path d="M76 16V4h10"/>
    <path d="M2 74h114"/><circle cx="20" cy="80" r="6"/><circle cx="46" cy="80" r="6"/><circle cx="72" cy="80" r="6"/><circle cx="98" cy="80" r="6"/>
  </svg>
  <h3>Farm Fuel</h3>
  <p>Looking for gasoline, diesel red diesel off road fuel or farm diesel?<br>We can deliver straight to your farm!&nbsp; We can setup your farm tanks, take care of EPA containment and deliver fuel when you need it!</p>
</div>

<div class="abs frame" style="left:619px;top:2346px;width:503px;height:379px">
  <div class="ph" role="img" aria-label="Photograph of a grey steel cargo container on gravel" style="background:linear-gradient(180deg,#c6cacd 0%,#a3a8ac 40%,#8f9296 70%,#77736b 100%)"></div>
</div>
<div class="abs svc" style="left:89px;top:2452px">
  <svg width="140" height="84" viewBox="0 0 140 84" fill="none" stroke="#222" stroke-width="3.5">
    <rect x="6" y="4" width="128" height="52"/><path d="M22 14v32M34 14v32M46 14v32M58 14v32M70 14v32M82 14v32M94 14v32M106 14v32M118 14v32"/>
    <path d="M2 62h136"/><circle cx="22" cy="72" r="7"/><circle cx="50" cy="72" r="7"/><circle cx="90" cy="72" r="7"/><circle cx="118" cy="72" r="7"/>
  </svg>
  <h3>Cargo Containers</h3>
  <p>Looking for gasoline, diesel red diesel off road fuel or farm diesel?<br>We can deliver straight to your farm!&nbsp; We can setup your farm tanks, take care of EPA containment and deliver fuel when you need it!</p>
</div>

<!-- blogs -->
<h2 class="abs slab section-title" style="top:2772px">Blogs</h2>

<article class="abs blog" style="left:82px">
  <div class="ph" role="img" aria-label="Photograph of a fuel tanker trailer parked by bare trees" style="background:linear-gradient(180deg,#c9cdd0 0%,#8c8a86 55%,#9a9995 100%)"></div>
  <span class="link"><svg width="22" height="22" viewBox="0 0 24 24" fill="none" stroke="#fff" stroke-width="2.2"><path d="M10 14a4 4 0 0 0 5.7 0l3-3a4 4 0 0 0-5.7-5.7l-1 1"/><path d="M14 10a4 4 0 0 0-5.7 0l-3 3a4 4 0 0 0 5.7 5.7l1-1"/></svg></span>
  <div class="head"><h4>Blog # 1</h4><time>July 17.2018</time></div>
  <p>Lorem Ipsum is simply a dummy text of the printing and typesetting industry.</p>
  <div class="meta"><span class="read">Read Full Artcle</span>
    <span class="count"><svg width="14" height="13" viewBox="0 0 24 22" fill="none" stroke="var(--red)" stroke-width="2.2"><path d="M12 20S2 13.5 2 7.5A5 5 0 0 1 12 5a5 5 0 0 1 10 2.5C22 13.5 12 20 12 20z"/></svg>35</span>
    <span class="count"><svg width="14" height="13" viewBox="0 0 24 22" fill="none" stroke="var(--red)" stroke-width="2.2"><path d="M4 4h16v11H9l-5 4z"/></svg>20</span>
  </div>
</article>

<article class="abs blog" style="left:440px">
  <div class="ph" role="img" aria-label="Photograph of car batteries stacked on a shop shelf" style="background:linear-gradient(160deg,#9aa39a 0%,#2f3a33 45%,#1d1e20 70%,#7a2a28 100%)"></div>
  <span class="link"><svg width="22" height="22" viewBox="0 0 24 24" fill="none" stroke="#fff" stroke-width="2.2"><path d="M10 14a4 4 0 0 0 5.7 0l3-3a4 4 0 0 0-5.7-5.7l-1 1"/><path d="M14 10a4 4 0 0 0-5.7 0l-3 3a4 4 0 0 0 5.7 5.7l1-1"/></svg></span>
  <div class="head"><h4>Blog # 2</h4><time>July 17.2018</time></div>
  <p>Lorem Ipsum is simply a dummy text of the printing and typesetting industry.</p>
  <div class="meta"><span class="read">Read Full Artcle</span>
    <span class="count"><svg width="14" height="13" viewBox="0 0 24 22" fill="none" stroke="var(--red)" stroke-width="2.2"><path d="M12 20S2 13.5 2 7.5A5 5 0 0 1 12 5a5 5 0 0 1 10 2.5C22 13.5 12 20 12 20z"/></svg>40</span>
    <span class="count"><svg width="14" height="13" viewBox="0 0 24 22" fill="none" stroke="var(--red)" stroke-width="2.2"><path d="M4 4h16v11H9l-5 4z"/></svg>23</span>
  </div>
</article>

<article class="abs blog" style="left:797px">
  <div class="ph" role="img" aria-label="Photograph of a white delivery truck under a carport" style="background:linear-gradient(135deg,#6c6a66 0%,#b9bab8 45%,#e2e2e0 65%,#7b7e80 100%)"></div>
  <span class="link"><svg width="22" height="22" viewBox="0 0 24 24" fill="none" stroke="#fff" stroke-width="2.2"><path d="M10 14a4 4 0 0 0 5.7 0l3-3a4 4 0 0 0-5.7-5.7l-1 1"/><path d="M14 10a4 4 0 0 0-5.7 0l-3 3a4 4 0 0 0 5.7 5.7l1-1"/></svg></span>
  <div class="head"><h4>Blog # 3</h4><time>July 17.2018</time></div>
  <p>Lorem Ipsum is simply a dummy text of the printing and typesetting industry.</p>
  <div class="meta"><span class="read">Read Full Artcle</span>
    <span class="count"><svg width="14" height="13" viewBox="0 0 24 22" fill="none" stroke="var(--red)" stroke-width="2.2"><path d="M12 20S2 13.5 2 7.5A5 5 0 0 1 12 5a5 5 0 0 1 10 2.5C22 13.5 12 20 12 20z"/></svg>25</span>
    <span class="count"><svg width="14" height="13" viewBox="0 0 24 22" fill="none" stroke="var(--red)" stroke-width="2.2"><path d="M4 4h16v11H9l-5 4z"/></svg>20</span>
  </div>
</article>

<div class="abs btn" style="left:514px;top:3270px;width:176px;height:47px;line-height:47px">View&nbsp; More</div>

<!-- testimonials -->
<h2 class="abs slab section-title" style="top:3362px;letter-spacing:1.5px">What Client Say</h2>

<div class="abs quote-card" style="left:80px;width:507px"></div>
<div class="abs quote-mark" style="left:157px">&ldquo;</div>
<div class="abs avatar" style="left:130px;top:3486px" role="img" aria-label="Portrait photo of the client"></div>
<div class="abs quote-name" style="left:262px;top:3494px">Dalton</div>
<p class="abs quote-text" style="left:266px;top:3532px">Lorem Ipsum&nbsp; simply dummy text printing and typesetting industry&nbsp; simply dummy a psum is is a simply dummy</p>
<div class="abs stars" style="left:266px;top:3606px">
  <svg width="13" height="13" viewBox="0 0 24 24"><path fill="var(--star)" d="M12 2l3 7h7l-5.6 4.5 2 7.5L12 16.8 5.6 21l2-7.5L2 9h7z"/></svg><svg width="13" height="13" viewBox="0 0 24 24"><path fill="var(--star)" d="M12 2l3 7h7l-5.6 4.5 2 7.5L12 16.8 5.6 21l2-7.5L2 9h7z"/></svg><svg width="13" height="13" viewBox="0 0 24 24"><path fill="var(--star)" d="M12 2l3 7h7l-5.6 4.5 2 7.5L12 16.8 5.6 21l2-7.5L2 9h7z"/></svg><svg width="13" height="13" viewBox="0 0 24 24"><path fill="var(--star)" d="M12 2l3 7h7l-5.6 4.5 2 7.5L12 16.8 5.6 21l2-7.5L2 9h7z"/></svg><svg width="13" height="13" viewBox="0 0 24 24"><path fill="var(--star)" d="M12 2l3 7h7l-5.6 4.5 2 7.5L12 16.8 5.6 21l2-7.5L2 9h7z"/></svg>
</div>

<div class="abs quote-card" style="left:621px;width:501px"></div>
<div class="abs quote-mark" style="left:696px">&ldquo;</div>
<div class="abs avatar" style="left:662px;top:3486px" role="img" aria-label="Portrait photo of the client"></div>
<div class="abs quote-name" style="left:796px;top:3494px">Harwell</div>
<p class="abs quote-text" style="left:800px;top:3532px">Lorem Ipsum&nbsp; simply dummy text printing and typesetting industry&nbsp; simply dummy a psum is is a simply dummy</p>
<div class="abs stars" style="left:800px;top:3606px">
  <svg width="13" height="13" viewBox="0 0 24 24"><path fill="var(--star)" d="M12 2l3 7h7l-5.6 4.5 2 7.5L12 16.8 5.6 21l2-7.5L2 9h7z"/></svg><svg width="13" height="13" viewBox="0 0 24 24"><path fill="var(--star)" d="M12 2l3 7h7l-5.6 4.5 2 7.5L12 16.8 5.6 21l2-7.5L2 9h7z"/></svg><svg width="13" height="13" viewBox="0 0 24 24"><path fill="var(--star)" d="M12 2l3 7h7l-5.6 4.5 2 7.5L12 16.8 5.6 21l2-7.5L2 9h7z"/></svg><svg width="13" height="13" viewBox="0 0 24 24"><path fill="var(--star)" d="M12 2l3 7h7l-5.6 4.5 2 7.5L12 16.8 5.6 21l2-7.5L2 9h7z"/></svg><svg width="13" height="13" viewBox="0 0 24 24"><path fill="var(--star)" d="M12 2l3 7h7l-5.6 4.5 2 7.5L12 16.8 5.6 21l2-7.5L2 9h7z"/></svg>
</div>

<div class="abs dots"><span></span><span></span><span></span></div>

<!-- footer -->
<footer class="abs footer"></footer>
<div class="abs foot-badge"><span>Brantley<br>Fuel</span></div>

<h4 class="abs foot-h" style="left:386px;top:3812px">Quick Link</h4>
<ul class="abs foot-list links" style="left:386px;top:3856px">
  <li>Home</li><li>About</li><li>Services</li><li>Blogs</li><li>Testimonials</li><li>Contact</li>
</ul>

<h4 class="abs foot-h" style="left:635px;top:3812px">Contact us</h4>
<ul class="abs foot-list contact" style="left:635px;top:3856px;width:200px">
  <li><svg width="10" height="13" viewBox="0 0 20 26"><path fill="#eee" d="M10 0a10 10 0 0 0-10 10c0 7 10 16 10 16s10-9 10-16A10 10 0 0 0 10 0zm0 14a4 4 0 1 1 0-8 4 4 0 0 1 0 8z"/></svg><span>4820 Mercer Road,<br>Halden Avenue,<br>USA</span></li>
  <li><svg width="11" height="11" viewBox="0 0 24 24"><path fill="#eee" d="M6.6 10.8a15.1 15.1 0 0 0 6.6 6.6l2.2-2.2a1 1 0 0 1 1-.25 11.4 11.4 0 0 0 3.6.57 1 1 0 0 1 1 1V20a1 1 0 0 1-1 1A17 17 0 0 1 3 4a1 1 0 0 1 1-1h3.5a1 1 0 0 1 1 1c0 1.25.2 2.45.57 3.57a1 1 0 0 1-.25 1z"/></svg><span>+014-228-7755</span></li>
  <li><svg width="11" height="11" viewBox="0 0 24 24"><path fill="#eee" d="M6 2h12v6H6zM3 9h18v9h-3v4H6v-4H3zm5 6v5h8v-5z"/></svg><span>+014-228-7755</span></li>
  <li><svg width="11" height="9" viewBox="0 0 24 18"><path fill="#eee" d="M0 0h24v18H0zm2 2v1l10 7 10-7V2z"/></svg><span>info@brantleyfuel.com</span></li>
</ul>

<h4 class="abs foot-h" style="left:862px;top:3812px">Sign up for Newsletter</h4>
<p class="abs" style="left:866px;top:3855px;width:260px;font-size:13px;line-height:1.3;color:var(--footer-text)">Lorem Ipsum is simply dummy&nbsp; the printing and typesetting industry</p>
<div class="abs news-input">Email Here</div>
<div class="abs subscribe">Subscribe</div>

<p class="abs copyright">&copy; Copyright 2019 Brantley Fuel. All Rights Reserved</p>
<div class="abs social bottom"><span></span><span></span><span></span><span></span></div>

</body>
</html>
```